Snack label design for chocolate covered snack

I uploaded sample I made .

I need more professional looking and for it to look extemly yum and authentic and stand out on shelves

Hi I’m looking to sell a snack called tolly wickets it’s basically Plove mix with chocolate and powder on the outside.

I will be selling it in a stand up pouch in 2 sizes and 3 flavors .

I have a few ideas of designs but I don’t love any .

I want a very professional classy attractive design to be made for my snack sticker.

It will come in 3 flavors and 2 sizes but the design will all be be based off one concept.

Please look at my files for ideas I made on my phone already.

If I pick you as winner I will need you to made the same sticker in 3 flavors … chocolate & peanut butter / brownie burst / cookies and cream

My Company is designing a new snack back I would like you to submit a sample idea of how you would design it . If I like your design I will hire you to make it .

I am only offering 3 designer this opportunity so please let me know if you would like to try for this.

I am basically looking for only one Design idea with logo that I will need 3 similar variations of since I will be having 3 flavors & 2 sizes of Chocolate & peanut butter / cookies and cream / brownie burst .

I would like the design to be classy catchy and modern . It should catch the eye of anyone who glances at it and should look very appealing and appetizing .

The design for example if you are making the chocolate peanut butter one it should clearly show Tolly wickets with chocolate and peanuts.

The name of my snack is
vellorinks
and the slogan is
chocolate powdered crunch

I attached a few samples of ideas and images I was working with land making myself but I want way more professional and attractive than this.

Please submit your idea as soon as possible so we can potential work together ty !

It’s very important that image of my snack that is tolly wickets looks classy very attractive real and appetizing

Grocery store shoppers

• Extremely apitizing and classy and stand out

```html
<!DOCTYPE html>
<html lang="en">
<head>
<meta charset="utf-8">
<title>Vellorinks – Chocolate &amp; Peanut Butter Pouch Label</title>
<link href="https://fonts.googleapis.com/css2?family=Bebas+Neue&family=Montserrat:wght@700&family=Allura&display=swap" rel="stylesheet">
<style>
  :root {
    --backdrop: #a9a9a9;
    --side-panel: #222222;
    --pouch-black: #0f0f0f;
    --seal-brown: #7b3b1c;
    --accent-orange: #c8680a;
    --logo-orange: #d88d1c;
    --ink-white: #f2f2f2;
    --snack-light: #b9aba6;
    --snack-dark: #5a4640;
  }
  * { margin: 0; padding: 0; box-sizing: border-box; }
  html, body { width: 978px; height: 1200px; overflow: hidden; }
  body { background: var(--backdrop); position: relative; }

  .side-panel {
    position: absolute; left: 0; top: 0; width: 355px; height: 1200px;
    background: var(--side-panel);
  }
  .side-panel__brand {
    position: absolute; left: 130px; top: 606px;
    transform: translate(-50%, -50%) rotate(-90deg);
    white-space: nowrap; color: var(--logo-orange);
    font-family: "Bebas Neue", sans-serif; font-size: 205px;
    line-height: 1; letter-spacing: 8px;
  }

  .label {
    position: absolute; left: 235px; top: 81px;
    width: 695px; height: 1043px;
    background: var(--pouch-black);
    border-radius: 18px 18px 8px 8px;
    overflow: hidden;
  }
  .seal-band {
    position: absolute; left: 0; top: 0; width: 100%; height: 80px;
    background: var(--seal-brown);
  }
  .seal-band__scallop {
    position: absolute; left: 0; top: 80px; width: 100%; height: 8px;
    background: radial-gradient(circle at 50% 0, var(--seal-brown) 6px, transparent 7px) repeat-x;
    background-size: 16px 8px;
  }

  .brand {
    position: absolute; left: 0; top: 124px; width: 100%;
    text-align: center; color: var(--logo-orange);
    font-family: "Bebas Neue", sans-serif; font-size: 92px;
    line-height: 1; letter-spacing: 3px;
  }
  .tagline {
    position: absolute; left: 0; top: 213px; width: 100%;
    text-align: center; color: var(--ink-white);
    font-family: "Montserrat", sans-serif; font-weight: 700;
    font-size: 12px; line-height: 1; letter-spacing: 5px;
  }
  .craft-note {
    position: absolute; left: 0; top: 238px; width: 100%;
    text-align: center; color: var(--ink-white);
    font-family: "Allura", cursive; font-size: 32px; line-height: 1;
  }
  .flavour {
    position: absolute; left: 0; top: 330px; width: 100%;
    text-align: center; color: var(--ink-white); font-weight: 400;
    font-family: "Bebas Neue", sans-serif; font-size: 98px;
    line-height: 78px; letter-spacing: 1px;
  }

  .rule {
    position: absolute; left: 0; width: 100%; height: 11px;
    background: var(--accent-orange);
  }
  .rule--top { top: 505px; }
  .rule--bottom { top: 904px; }

  .snack-photo {
    position: absolute; left: 0; top: 516px; width: 100%; height: 388px;
    background:
      radial-gradient(ellipse at 30% 40%, rgba(255,255,255,0.18), transparent 60%),
      linear-gradient(160deg, var(--snack-light), var(--snack-dark));
  }

  .weight {
    position: absolute; left: 62px; top: 958px;
    color: var(--ink-white);
    font-family: "Bebas Neue", sans-serif; font-size: 54px; line-height: 1;
  }
  .natural-badge {
    position: absolute; left: 377px; top: 796px; width: 318px; height: 247px;
  }
  .natural-badge__pct,
  .natural-badge__word {
    position: absolute; right: 60px; text-align: right; color: var(--ink-white);
    font-family: "Bebas Neue", sans-serif; line-height: 1;
  }
  .natural-badge__pct { top: 893px; font-size: 58px; }
  .natural-badge__word { top: 943px; font-size: 86px; }
</style>
</head>
<body>
  <div class="side-panel">
    <div class="side-panel__brand">VELLORINKS</div>
  </div>

  <div class="label">
    <div class="seal-band"></div>
    <div class="seal-band__scallop"></div>

    <div class="brand">VELLORINKS</div>
    <div class="tagline">CHOCOLATE POWDERED CRUNCH</div>
    <div class="craft-note">Handcrafted snack</div>

    <h1 class="flavour">CHOCOLATE &amp;<br>PEANUT BUTTER</h1>

    <div class="rule rule--top"></div>
    <div class="snack-photo" role="img" aria-label="Close-up photo of powdered chocolate peanut butter cereal snack pieces"></div>
    <div class="rule rule--bottom"></div>

    <div class="weight">500G</div>

    <svg class="natural-badge" viewBox="0 0 318 247" aria-hidden="true">
      <circle cx="360" cy="380" r="380" fill="var(--accent-orange)"/>
      <circle cx="368" cy="388" r="345" fill="none" stroke="var(--pouch-black)" stroke-width="3"/>
    </svg>
    <div class="natural-badge__pct">100%</div>
    <div class="natural-badge__word">NATURAL</div>
  </div>
</body>
</html>
```